I want to revise my business card design and get a more modern and up to date design.

uMendo Handyman Sevices originated from a family-owned and operated contractor business, performing home renovation, addition, and construction work in the NYC area since 2004. Today, we specialize in reliable and affordable handyman services for residential and commercial clients In 2014, we expanded to northern New Jersey. In 2016, we brought quality home improvement and repair services to new Bucks County, PA, and nearby New Jersey areas.
Target Market(s)
Home owners and business that might be looking for a General contractor, handyman, cleaning services and Home maintenance and property.
Industry/Entity Type
Construction Company
Contact Information for Business Card
I am open to new ideas
Colors
Designer to choose colors to be used in the design.
Look and feel

```html
<!DOCTYPE html>
<html lang="en">
<head>
<meta charset="utf-8">
<title>uMendo Handyman Sevices – Business Card</title>
<link rel="stylesheet" href="https://fonts.googleapis.com/css2?family=Roboto:wght@400;500;700;900&display=swap">
<style>
  :root {
    --brand-red: #e01b22;
    --deep-red: #b3141a;
    --accent-yellow: #f2c21b;
    --ink: #1c1c1c;
    --paper: #ffffff;
    --paper-shade: #eeeeee;
    --backdrop: #2e2e30;
    --reverse-text: #e9e9e9;
  }
  * { box-sizing: border-box; margin: 0; padding: 0; }
  html, body { width: 1200px; height: 900px; overflow: hidden; }
  body {
    background: var(--backdrop);
    font-family: "Roboto", Arial, sans-serif;
    display: flex;
    flex-direction: column;
    align-items: center;
    justify-content: center;
    gap: 50px;
  }
  .card {
    position: relative;
    width: 630px;
    height: 360px;
    overflow: hidden;
    box-shadow: 0 14px 30px rgba(0,0,0,.45);
  }

  /* Front */
  .card-front {
    background: linear-gradient(135deg, var(--paper-shade) 0%, var(--paper) 45%, var(--paper) 100%);
  }
  .brand-mark {
    position: absolute;
    left: 40px; top: 38px;
    display: flex; align-items: center; gap: 12px;
  }
  .brand-square {
    width: 34px; height: 34px;
    background: var(--brand-red);
  }
  .brand-name {
    font-size: 26px; font-weight: 700; color: var(--ink);
    letter-spacing: .2px;
  }
  .divider {
    position: absolute;
    left: 40px; right: 70px; top: 150px;
    height: 1.5px;
    background: var(--brand-red);
  }
  .contact-list {
    position: absolute;
    left: 40px; top: 168px;
    list-style: none;
    font-size: 15px; color: var(--ink);
    line-height: 25px;
  }
  .contact-list li { display: flex; align-items: center; gap: 10px; }
  .contact-list svg { width: 12px; height: 12px; fill: var(--brand-red); }
  .person {
    position: absolute;
    right: 70px; top: 104px;
    text-align: right;
  }
  .person-name {
    font-size: 25px; font-weight: 500; color: var(--brand-red);
    text-transform: uppercase; letter-spacing: -.3px;
  }
  .person-role {
    font-size: 15px; color: var(--ink);
    position: absolute; right: 0; top: 52px;
    white-space: nowrap;
  }
  .address {
    position: absolute;
    right: 40px; bottom: 38px;
    text-align: right;
    font-size: 15px; font-weight: 500; color: var(--ink);
    line-height: 22px;
  }
  .footer-band { position: absolute; left: 0; bottom: 0; width: 630px; height: 110px; }

  /* Back */
  .card-back {
    background: radial-gradient(circle at 35% 30%, var(--brand-red) 0%, var(--deep-red) 100%);
    display: flex; align-items: center; justify-content: center; gap: 22px;
  }
  .card-back .brand-square {
    width: 64px; height: 64px;
    background: var(--reverse-text);
  }
  .card-back .brand-name {
    font-size: 46px; color: var(--reverse-text);
  }
</style>
</head>
<body>

  <section class="card card-front" aria-label="Front of business card">
    <div class="brand-mark">
      <span class="brand-square"></span>
      <span class="brand-name">uMendo Handyman Sevices</span>
    </div>

    <div class="person">
      <p class="person-name">Daniel Harper</p>
      <p class="person-role">Director</p>
    </div>

    <div class="divider"></div>

    <ul class="contact-list">
      <li>
        <svg viewBox="0 0 24 24"><path d="M6.6 10.8a15.1 15.1 0 0 0 6.6 6.6l2.2-2.2a1 1 0 0 1 1-.25 11.4 11.4 0 0 0 3.6.57 1 1 0 0 1 1 1V20a1 1 0 0 1-1 1A17 17 0 0 1 3 4a1 1 0 0 1 1-1h3.5a1 1 0 0 1 1 1c0 1.25.2 2.45.57 3.6a1 1 0 0 1-.25 1z"/></svg>
        (215) 555-0148
      </li>
      <li>
        <svg viewBox="0 0 24 24"><path d="M2 5h20v14H2zm2 2v.5l8 5 8-5V7zm0 2.8V17h16V9.8l-8 5z"/></svg>
        info@umendohs.com
      </li>
      <li>
        <svg viewBox="0 0 24 24"><circle cx="12" cy="12" r="10"/></svg>
        www.umendohs.com
      </li>
    </ul>

    <svg class="footer-band" viewBox="0 0 630 110" preserveAspectRatio="none" aria-hidden="true">
      <path d="M0 28 L250 88 L0 88 Z" fill="var(--accent-yellow)"/>
      <path d="M0 38 L255 96 C275 100 280 108 300 110 L0 110 Z" fill="var(--brand-red)"/>
      <rect x="0" y="100" width="630" height="10" fill="var(--brand-red)"/>
    </svg>

    <p class="address">148 Harbour Lane,<br>Riverton, NZ, 8024</p>
  </section>

  <section class="card card-back" aria-label="Back of business card">
    <span class="brand-square"></span>
    <span class="brand-name">uMendo Handyman Sevices</span>
  </section>

</body>
</html>
```